School Website

I need a design for a School (2 sections: Primary 6-12 years and Secondary 12-18 years). The first page is just a choice of the 2 sections. After we'll need 2 websites (with the same structure: Menu, ...) but with different colors. In fact, we need for end of October, 6 design of school website. So the best websites are going to be made available to you in the future (in pixelharbr) but privately.

Target Market(s)

Public, Parents, ...

Coding

Coded - Design and coding required

Number of Pages Required

5+ page

Font styles to use
Sans Serif

Colors
34a6d7
85cae6
cee9f5
ffffff

Requirements
Must have
• You can check the old Website: http: / /velmok.be We need the same pages with the same content. Menu: - HomePage - News and communication (like blog page) - Activities (like blog page, with photo gallery) - Contact (Contact form + maps) - In the main menu, we need a special button to connect to an external Website ( button needs to be different than the other menu items The name of this button is "Parents Area"). The logo of 2 sections are attached. Please use it for the design and the choice of colors.
Nice to have
• This is a web design of other school that we like: https://www.quintel.be

```html
<!DOCTYPE html>
<html lang="en">
<head>
<meta charset="utf-8">
<title>Royal Athenaeum of Velmont – Kindergarten and Primary</title>
<link href="https://fonts.googleapis.com/css2?family=Lato:wght@400;700;900&display=swap" rel="stylesheet">
<style>
:root{
  --blue:#34a6d7;
  --blue-mid:#85cae6;
  --blue-pale:#cee9f5;
  --blue-band:#bfe2f3;
  --blue-contact:#74bde0;
  --blue-deep:#2f8fcf;
  --white:#ffffff;
  --grey-bg:#f2f2f2;
  --ink:#2b2b2b;
  --text:#444444;
  --green:#5aaa2e;
  --footer:#2c2c2c;
}
*{box-sizing:border-box;margin:0;padding:0}
html,body{width:1200px;height:3435px;overflow:hidden}
body{font-family:'Lato',sans-serif;color:var(--text);background:var(--white);position:relative}
.abs{position:absolute}

.site-header{position:absolute;top:0;left:0;width:1200px;height:112px;background:var(--white)}
.brand{position:absolute;left:75px;top:22px;display:flex;align-items:center;gap:10px}
.brand-dot{width:44px;height:44px;border-radius:50%;background:var(--blue)}
.brand-name{font-weight:700;font-size:24px;color:var(--blue-deep)}
.main-nav{position:absolute;right:75px;top:34px;display:flex;align-items:center;gap:38px;font-size:15px;color:var(--ink);letter-spacing:.3px}
.main-nav .active{color:var(--blue);border-bottom:2px solid var(--blue);padding:8px 16px}
.parents-btn{background:var(--green);color:var(--white);padding:10px 16px;font-size:14px;font-weight:700;display:flex;align-items:center;gap:8px}

.hero{position:absolute;top:112px;left:0;width:1200px;height:572px;overflow:hidden;
  background:
    radial-gradient(ellipse 260px 300px at 560px 170px,#d7b49c 0%,rgba(215,180,156,0) 100%),
    radial-gradient(ellipse 220px 260px at 980px 380px,#e9c4b6 0%,rgba(233,196,182,0) 100%),
    radial-gradient(ellipse 200px 240px at 300px 390px,#d8c7b8 0%,rgba(216,199,184,0) 100%),
    linear-gradient(180deg,rgba(0,0,0,0) 70%,rgba(209,168,96,.55) 100%),
    linear-gradient(90deg,#9fae86 0%,#a89c86 30%,#8e8f80 55%,#6f7a66 80%,#5a6a55 100%)}
.hero-title{position:absolute;top:210px;width:1200px;text-align:center;color:var(--white);text-shadow:0 2px 6px rgba(0,0,0,.35)}
.hero-title .l1,.hero-title .l2{font-weight:900;font-size:53px;line-height:52px;display:block}
.hero-title .l3{font-weight:700;font-size:34px;display:block;margin-top:8px}
.hero-dots{position:absolute;top:530px;left:561px;display:flex;gap:10px}
.hero-dots span{width:11px;height:11px;border-radius:50%;background:var(--blue-mid)}
.hero-dots span:first-child{background:var(--white)}

.news-bar{position:absolute;top:684px;left:0;width:1200px;height:65px;background:var(--blue-pale);display:flex;align-items:center}
.news-label{width:253px;height:65px;background:var(--blue-mid);color:var(--white);font-weight:700;font-size:21px;display:flex;align-items:center;padding-left:74px}
.news-item{padding-left:24px;font-size:16px;color:var(--ink)}
.news-item b{color:var(--blue);margin-right:6px}
.news-item a{color:var(--blue-deep);font-size:13px;text-decoration:none}
.news-arrows{position:absolute;right:70px;top:24px;display:flex;gap:18px}

.features{position:absolute;top:749px;left:0;width:1200px;height:350px;background:var(--grey-bg)}
.feature-card{position:absolute;top:91px;width:330px;height:213px;background:var(--white);text-align:center}
.feature-icon{position:absolute;top:-53px;left:112px;width:106px;height:106px;border-radius:50%;background:var(--white);box-shadow:0 0 0 4px #e9e9e9;display:flex;align-items:center;justify-content:center}
.feature-card h3{margin-top:70px;color:var(--blue);font-size:17px;font-weight:900}
.feature-card p{margin:10px auto 0;width:280px;font-size:15px;line-height:22px}
.read-btn{display:inline-block;margin-top:18px;background:var(--blue-pale);color:var(--ink);font-size:13px;font-weight:700;padding:10px 21px}

.meals-band{position:absolute;top:1204px;left:0;width:1200px;height:408px;background:var(--blue-band)}
.comm-frame{position:absolute;top:1163px;left:73px;width:515px;height:490px;background:var(--white);border:1px solid #d6d6d6;padding:7px}
.comm-photo{width:100%;height:100%;display:flex;align-items:center;justify-content:center;
  background:
    radial-gradient(ellipse 120px 90px at 210px 400px,#e9c878 0%,rgba(233,200,120,0) 100%),
    linear-gradient(180deg,rgba(0,0,0,0) 55%,#e9e6de 80%,#d8d2c4 100%),
    linear-gradient(90deg,#6f6f6c 0%,#8b8a86 55%,#5fa6c0 60%,#b99c84 100%)}
.comm-photo span{color:var(--white);font-weight:700;font-size:35px;text-shadow:0 2px 5px rgba(0,0,0,.4)}
.meals-text{position:absolute;top:1278px;left:613px;width:520px}
.meals-text h2{font-size:27px;font-weight:900;color:var(--ink);margin-bottom:14px}
.meals-text p{font-size:17px;line-height:31px;color:var(--ink)}
.meals-phone{display:flex;gap:22px;margin-top:24px;align-items:flex-start}
.meals-phone .lbl{font-size:19px;font-weight:700;color:var(--ink)}
.meals-phone .num{font-size:29px;font-weight:700;color:var(--blue)}

.activities-title{position:absolute;top:1725px;width:1200px;text-align:center;font-size:33px;font-weight:900;color:var(--ink)}
.gallery-item{position:absolute}
.g-canteen{background:
  linear-gradient(180deg,#e4e1d8 0%,#d9d5c9 24%,rgba(0,0,0,0) 25%),
  linear-gradient(180deg,rgba(0,0,0,0) 25%,#7cb33e 26%,#6aa43a 48%,#b98a45 49%,#a8773a 100%)}
.g-hall{background:linear-gradient(180deg,#d9d7d0 0%,#cfcdc6 30%,#2e5d8e 31%,#2b557f 55%,#8c8a86 56%,#5a5856 100%)}
.g-gym{background:linear-gradient(180deg,#c98a5a 0%,#d8d2c6 18%,#cfc7b8 62%,#9a6a46 63%,#7c4e30 100%)}
.g-dining{background:linear-gradient(180deg,#ece8de 0%,#e2ddd0 30%,#7cad48 31%,#6b9e3c 55%,#b38346 56%,#8a6230 100%)}
.g-building{background:linear-gradient(180deg,#2a5fb8 0%,#3a6bb0 18%,#8e9aa4 19%,#5d6f84 62%,#9a9c98 63%,#7f8a74 100%)}

.contact-band{position:absolute;top:2333px;left:0;width:1200px;height:423px;background:var(--blue-contact)}
.contact-title{position:absolute;top:2380px;left:108px;font-size:34px;font-weight:900;color:var(--white)}
.field{position:absolute;background:var(--white);font-size:14px;color:var(--ink);padding:15px}
.submit-btn{position:absolute;top:2658px;left:108px;width:154px;height:45px;background:var(--blue-deep);color:var(--white);font-weight:700;font-size:16px;display:flex;align-items:center;justify-content:center}
.map-frame{position:absolute;top:2300px;left:613px;width:514px;height:489px;background:var(--white);border:1px solid #d6d6d6;padding:6px}
.map-area{height:355px;background:linear-gradient(160deg,#f3eedc,#e8efd9 50%,#dfe8cd);position:relative}
.map-info{height:120px;background:var(--blue-deep);color:var(--white);font-size:16px;text-align:center;padding-top:18px;line-height:31px}
.map-info div{display:flex;justify-content:center;align-items:center;gap:8px}

.useful-band{position:absolute;top:2917px;left:0;width:1200px;height:443px;background:var(--blue-band)}
.useful-icon{position:absolute;top:2864px;left:547px;width:106px;height:106px;border-radius:50%;background:var(--blue);border:5px solid var(--white)}
.useful-title{position:absolute;top:2990px;width:1200px;text-align:center;font-size:35px;font-weight:900;color:var(--white)}
.person-card{position:absolute;top:3073px;width:242px;height:240px;background:var(--white);text-align:center;padding:34px 14px 0}
.person-card.center{padding-top:22px}
.person-card h4{color:var(--blue);font-size:22px;font-weight:400;line-height:31px;margin-bottom:8px}
.person-card p{font-size:16px;line-height:25px;color:var(--ink)}
.carousel-arrow{position:absolute;top:3178px}

.site-footer{position:absolute;top:3360px;left:0;width:1200px;height:75px;background:var(--footer);color:var(--white)}
.copyright{position:absolute;left:108px;top:30px;font-size:13px}
.social{position:absolute;right:70px;top:28px;display:flex;gap:17px}
.social span{width:18px;height:18px;border:2px solid var(--white);border-radius:3px}
</style>
</head>
<body>

<header class="site-header">
  <div class="brand"><span class="brand-dot"></span><span class="brand-name">Lycée Royal de Velmont</span></div>
  <nav class="main-nav">
    <span class="active">HOME</span>
    <span>KINDERGARTEN-PRIMARY</span>
    <span>CONTACT</span>
    <span>PLAN</span>
    <span class="parents-btn">
      <svg width="16" height="12" viewBox="0 0 16 12" fill="#fff"><circle cx="5" cy="3" r="2.5"/><circle cx="11" cy="3" r="2.5"/><path d="M0 12c0-3 2-5 5-5s5 2 5 5zM8 12c0-3 1-5 3-5s5 2 5 5z"/></svg>
      PARENTS AREA</span>
  </nav>
</header>

<section class="hero" role="img" aria-label="Photo of a teacher sharing a meal with young children at a classroom table">
  <h1 class="hero-title">
    <span class="l1">WELCOME TO</span>
    <span class="l2">ROYAL ATHENAEUM OF VELMONT</span>
    <span class="l3">KINDERGARTEN AND PRIMARY</span>
  </h1>
  <div class="hero-dots"><span></span><span></span><span></span><span></span></div>
</section>

<div class="news-bar">
  <div class="news-label">LATEST NEWS</div>
  <div class="news-item"><b>SEPTEMBER 28, 2019:</b>Etiam vitae libero sit amet eros tempor varius...<a href="#">Read More</a></div>
  <div class="news-arrows">
    <svg width="10" height="16" viewBox="0 0 10 16"><path d="M8 2L2 8l6 6" stroke="#222" stroke-width="2.5" fill="none"/></svg>
    <svg width="10" height="16" viewBox="0 0 10 16"><path d="M2 2l6 6-6 6" stroke="#222" stroke-width="2.5" fill="none"/></svg>
  </div>
</div>

<section class="features">
  <div class="feature-card" style="left:75px">
    <div class="feature-icon"><svg width="56" height="56" viewBox="0 0 56 56"><rect x="10" y="6" width="30" height="40" rx="3" fill="#6cc3ec"/><g stroke="#1f5fa8" stroke-width="3"><path d="M16 18h18M16 25h18M16 32h12"/></g><path d="M36 40l12-16 4 3-12 16-5 1z" fill="#e94141"/></svg></div>
    <h3>RULES OF PROCEDURE</h3>
    <p>Class aptent taciti sociosqu ad litora torquent per conubia.</p>
    <span class="read-btn">READ MORE</span>
  </div>
  <div class="feature-card" style="left:435px">
    <div class="feature-icon"><svg width="60" height="56" viewBox="0 0 60 56"><circle cx="14" cy="14" r="6" fill="#f5a623"/><path d="M22 26a18 14 0 0 1 34 0z" fill="#e94141"/><path d="M39 26l-6 20" stroke="#333" stroke-width="2"/><path d="M6 46q24-8 50 0v4H6z" fill="#f5c242"/><path d="M4 50h52" stroke="#34a6d7" stroke-width="4"/></svg></div>
    <h3>SCHOOL HOLIDAYS</h3>
    <p>Class aptent taciti sociosqu ad litora torquent per conubia.</p>
    <span class="read-btn">READ MORE</span>
  </div>
  <div class="feature-card" style="left:796px">
    <div class="feature-icon"><svg width="60" height="60" viewBox="0 0 60 60"><circle cx="28" cy="28" r="22" fill="#fff" stroke="#3b4a5a" stroke-width="4"/><path d="M28 14v14h9" stroke="#3b4a5a" stroke-width="3" fill="none"/><circle cx="44" cy="44" r="10" fill="#3cb878"/><path d="M39 44l4 4 6-7" stroke="#fff" stroke-width="2.5" fill="none"/></svg></div>
    <h3>OUR SCHEDULES &amp; DAYCARE</h3>
    <p>Class aptent taciti sociosqu ad litora torquent per conubia.</p>
    <span class="read-btn">READ MORE</span>
  </div>
</section>

<div class="meals-band"></div>
<div class="comm-frame">
  <div class="comm-photo" role="img" aria-label="Photo of children eating lunch together at a school table"><span>COMMUNICATIONS</span></div>
</div>
<div class="meals-text">
  <h2>MEALS OFFERED !!!</h2>
  <p>To the children&nbsp; of the nursery section of LE LYCÉE ROYAL DE VELMONT&nbsp; during the whole school year!<br>Pilot project for your little ones, our little ones&nbsp; of the LR VELMONT. Which team</p>
  <div class="meals-phone">
    <svg width="36" height="36" viewBox="0 0 24 24" style="margin-top:6px"><path fill="#2b2b2b" d="M6.6 10.8a15 15 0 0 0 6.6 6.6l2.2-2.2a1 1 0 0 1 1-.25 11.4 11.4 0 0 0 3.6.57 1 1 0 0 1 1 1V20a1 1 0 0 1-1 1A17 17 0 0 1 3 4a1 1 0 0 1 1-1h3.5a1 1 0 0 1 1 1 11.4 11.4 0 0 0 .57 3.6 1 1 0 0 1-.25 1z"/></svg>
    <div><div class="lbl">Information and registration on</div><div class="num">081 47 30 52</div></div>
  </div>
</div>

<h2 class="activities-title">ACTIVITIES</h2>
<div class="gallery-item g-canteen" style="left:75px;top:1797px;width:512px;height:423px" role="img" aria-label="Photo of a school canteen with green walls and rows of tables"></div>
<div class="gallery-item g-hall" style="left:613px;top:1797px;width:243px;height:198px" role="img" aria-label="Photo of a school hallway with a patterned floor"></div>
<div class="gallery-item g-gym" style="left:883px;top:1797px;width:244px;height:198px" role="img" aria-label="Photo of an empty school gymnasium"></div>
<div class="gallery-item g-dining" style="left:613px;top:2023px;width:243px;height:197px" role="img" aria-label="Photo of a school dining room"></div>
<div class="gallery-item g-building" style="left:883px;top:2023px;width:244px;height:197px" role="img" aria-label="Photo of the school building exterior"></div>

<section class="contact-band"></section>
<h2 class="contact-title">CONTACT US</h2>
<div class="field" style="left:108px;top:2438px;width:234px;height:46px">Enter Name</div>
<div class="field" style="left:354px;top:2438px;width:233px;height:46px">Enter Email Address</div>
<div class="field" style="left:108px;top:2494px;width:479px;height:146px;padding-top:20px">Comments</div>
<div class="submit-btn">SUBMIT</div>

<div class="map-frame">
  <div class="map-area" role="img" aria-label="Map of the region showing the school location">
    <svg class="abs" style="left:252px;top:150px" width="30" height="40" viewBox="0 0 30 40"><path d="M15 0a15 15 0 0 1 15 15c0 11-15 25-15 25S0 26 0 15A15 15 0 0 1 15 0z" fill="#e53935"/><circle cx="15" cy="15" r="5" fill="#fff"/></svg>
  </div>
  <div class="map-info">
    <div><svg width="11" height="14" viewBox="0 0 11 14"><path d="M5.5 0A5.5 5.5 0 0 1 11 5.5C11 9.5 5.5 14 5.5 14S0 9.5 0 5.5A5.5 5.5 0 0 1 5.5 0z" fill="#fff"/><circle cx="5.5" cy="5.5" r="2" fill="#2f8fcf"/></svg>Rue des Tilleuls 1 / A, 4520 Velmont, Belgium</div>
    <div><svg width="13" height="13" viewBox="0 0 24 24"><path fill="#fff" d="M6.6 10.8a15 15 0 0 0 6.6 6.6l2.2-2.2a1 1 0 0 1 1-.25 11.4 11.4 0 0 0 3.6.57 1 1 0 0 1 1 1V20a1 1 0 0 1-1 1A17 17 0 0 1 3 4a1 1 0 0 1 1-1h3.5a1 1 0 0 1 1 1 11.4 11.4 0 0 0 .57 3.6 1 1 0 0 1-.25 1z"/></svg>+32 81 47 30 52</div>
    <div><svg width="14" height="14" viewBox="0 0 14 14"><circle cx="7" cy="7" r="6" fill="none" stroke="#fff" stroke-width="1.6"/><path d="M7 3.5V7h3" stroke="#fff" stroke-width="1.6" fill="none"/></svg>Monday to Friday: 7 am - 6 pm</div>
  </div>
</div>

<section class="useful-band"></section>
<div class="useful-icon">
  <svg width="96" height="96" viewBox="0 0 96 96"><g fill="#fff"><circle cx="48" cy="28" r="8"/><circle cx="30" cy="52" r="8"/><circle cx="66" cy="52" r="8"/></g><g fill="#1f3a5a"><path d="M36 48q12-10 24 0v2H36z"/><path d="M18 72q12-10 24 0v4H18z"/><path d="M54 72q12-10 24 0v4H54z"/></g></svg>
</div>
<h2 class="useful-title">USEFUL CONTACTS</h2>
<svg class="carousel-arrow" style="left:46px" width="14" height="26" viewBox="0 0 14 26"><path d="M12 2L2 13l10 11" stroke="#2b2b2b" stroke-width="2" fill="none"/></svg>
<div class="person-card" style="left:75px">
  <h4>Mrs Sophie LAMBERT</h4>
  <p>Prefect of studies<br>Quai des Saules, 5 - 4520<br>VELMONT 081 / 64.21.90</p>
</div>
<div class="person-card center" style="left:344px">
  <h4>Madame Claire<br>DUMONT</h4>
  <p>Director of the<br>fundamental section<br>Rue des Tilleuls,<br>1a - 4520 VELMONT<br>081 / 47.30.52</p>
</div>
<div class="person-card" style="left:615px">
  <h4>Mrs Laura<br>MARCHAL</h4>
  <p>Secretariat<br>Rue des Tilleuls,<br>1a - 4520 VELMONT<br>081 / 47.30.52</p>
</div>
<div class="person-card" style="left:884px">
  <h4>Mrs Elise<br>VERMEULEN</h4>
  <p>Administrative help<br>Rue des Tilleuls,<br>1a - 4520 VELMONT</p>
</div>
<svg class="carousel-arrow" style="left:1140px" width="14" height="26" viewBox="0 0 14 26"><path d="M2 2l10 11L2 24" stroke="#2b2b2b" stroke-width="2" fill="none"/></svg>

<footer class="site-footer">
  <div class="copyright">Copyright © 2019. Company Name. All Right Reserved</div>
  <div class="social" aria-label="Social network links"><span></span><span></span><span></span><span></span><span></span></div>
</footer>

</body>
</html>
```